Help us create a stunning photo image for our website

Creative and eye catching photo - something different but still classy and professional for modern law firm practicing family and property law. We would love you to play with a photo of your choice and make it unique - by changing it somehow so it doesn’t look like just another stock standard photo - the slogan is “Experience and Results”.

Target Market(s)

Young - Mid life professionals - both men and women

Font styles to use
Serif
Sans Serif

Requirements
Must have
• Originality and personality to stand out from the crowd - must grab attention and be a photo you have edited in some way to make it look unique - the rest is up to you
Should not have
• No cartoons and no animals

```html
<!DOCTYPE html>
<html lang="en">
<head>
<meta charset="UTF-8">
<title>Experience and Results</title>
<link href="https://fonts.googleapis.com/css2?family=Bodoni+Moda:wght@400;500&display=swap" rel="stylesheet">
<style>
  :root {
    --page: #ffffff;
    --ink-green: #4a7868;
    --sage: #86a69d;
    --sky-top: #6fa9c2;
    --sky-mid: #a9d2e0;
    --horizon: #eef0ea;
    --rock-warm: #c9ab78;
    --rock-dark: #5c5549;
  }
  * { margin: 0; padding: 0; box-sizing: border-box; }
  html, body {
    width: 1200px;
    height: 834px;
    overflow: hidden;
    background: var(--page);
  }
  .canvas {
    position: relative;
    width: 1200px;
    height: 834px;
    background: var(--page);
  }
  .hero-photo {
    position: absolute;
    left: 63px;
    top: 51px;
    width: 1069px;
    height: 712px;
    background:
      radial-gradient(ellipse 260px 220px at 585px 510px, rgba(255,250,228,0.95), rgba(255,240,200,0.5) 45%, rgba(255,240,200,0) 75%),
      radial-gradient(ellipse 520px 320px at 560px 620px, rgba(214,180,120,0.55), rgba(214,180,120,0) 70%),
      linear-gradient(180deg, var(--sky-top) 0%, var(--sky-mid) 30%, var(--horizon) 62%, var(--rock-warm) 74%, #8f7c5e 86%, var(--rock-dark) 100%);
  }
  .title-card {
    position: absolute;
    left: 761px;
    top: 97px;
    width: 342px;
    height: 396px;
    background: var(--page);
    text-align: center;
  }
  .slogan {
    font-family: "Bodoni Moda", "Didot", serif;
    font-weight: 400;
    color: var(--ink-green);
    font-size: 49px;
    line-height: 61px;
    letter-spacing: 0.07em;
    padding-top: 12px;
    padding-left: 0.07em;
  }
  .slogan span { display: block; }
  .slogan-rule {
    position: absolute;
    left: 94px;
    top: 196px;
    width: 161px;
    height: 3px;
    background: var(--ink-green);
  }
  .title-band {
    position: absolute;
    left: 761px;
    top: 493px;
    width: 342px;
    height: 54px;
    background: var(--sage);
  }
  .dot {
    position: absolute;
    width: 84px;
    height: 84px;
    border-radius: 50%;
    background: var(--sage);
  }
  .dot--card { left: 712px; top: 175px; }
  .dot--one { left: 142px; top: 628px; }
  .dot--two { left: 267px; top: 626px; }
  .dot--three { left: 388px; top: 627px; }
</style>
</head>
<body>
  <main class="canvas">
    <div class="hero-photo" role="img" aria-label="Photo: a person standing on a rocky mountain summit with arms outstretched, backlit by the rising sun against a clear blue sky"></div>

    <section class="title-card">
      <h1 class="slogan">
        <span>Experience</span>
        <span>and</span>
        <span>Results</span>
      </h1>
      <div class="slogan-rule"></div>
    </section>
    <div class="title-band"></div>

    <div class="dot dot--card"></div>
    <div class="dot dot--one"></div>
    <div class="dot dot--two"></div>
    <div class="dot dot--three"></div>
  </main>
</body>
</html>
```